Business card and stationary designs for Harbor Summit Mentor
Harbor Summit Mentor
Business card and stationary designs for Harbor Summit Mentor - Consulting
Creative Brief
Professional
Reed Calloway
Executive & Professional Coach
4187 Willow Bend Lane Dallas TX 75231
RCalloway@harborsummitmentor.example
www.HarborSummitMentor.example
I want this to look clean, cutting edge, and for the design to stand out.
On the back of the business card I would like my logo and the phrase "Executive & Professional Coaching"

```html
<!DOCTYPE html>
<html lang="en">
<head>
<meta charset="utf-8">
<title>Harbor Summit Mentor – Stationery Set</title>
<link rel="stylesheet" href="https://fonts.googleapis.com/css2?family=Cinzel:wght@400;600&family=Lato:wght@300;400;700&display=swap">
<style>
  :root{
    --bg:#e6e6e6;
    --paper:#ffffff;
    --ink:#2b2b2b;
    --charcoal:#3a3a3a;
    --charcoal-deep:#262626;
    --band:#4a4a4a;
    --muted:#8a8a8a;
    --light-text:#e9e9e9;
  }
  *{box-sizing:border-box;margin:0;padding:0}
  html,body{width:1200px;height:936px;overflow:hidden;background:var(--bg)}
  body{position:relative;font-family:"Lato",sans-serif;color:var(--ink)}
  .piece{position:absolute;background:var(--paper)}
  .brand{font-family:"Cinzel",serif;font-weight:400;color:var(--ink);letter-spacing:.04em;line-height:1.05;display:flex;align-items:center;gap:8px}
  .brand .mark{width:9px;height:9px;border:1px solid currentColor;border-radius:50%;flex:none}

  /* Letterhead */
  .letterhead{left:25px;top:25px;width:565px;height:690px;padding:36px 48px 0}
  .letterhead .brand{font-size:20px}
  .letter-body{margin-top:52px;font-size:7.5px;line-height:1.6;color:#555}
  .letter-body p{margin-bottom:10px}
  .letter-body .gap{margin-top:14px}
  .signature{width:46px;height:18px;margin:8px 0 6px;background:linear-gradient(90deg,#bbb,#e2e2e2)}
  .letter-footer{position:absolute;left:0;right:0;bottom:0}
  .letter-footer .address{text-align:center;font-size:7px;color:var(--muted);padding-bottom:6px}
  .letter-footer .url-band{background:var(--charcoal);color:var(--light-text);text-align:center;font-size:9px;letter-spacing:.18em;padding:7px 0}
  .letter-footer .base{height:32px}

  /* Presentation folder */
  .folder{left:630px;top:25px;width:545px;height:700px;background:var(--charcoal-deep)}
  .folder .texture{position:absolute;inset:0;background:linear-gradient(160deg,#3d3d3d,#222 55%,#2e2e2e)}
  .folder .center-strip{position:absolute;top:0;bottom:44px;left:50%;width:90px;transform:translateX(-50%);background:linear-gradient(90deg,rgba(255,255,255,0),rgba(255,255,255,.06),rgba(255,255,255,0))}
  .folder .brand{position:absolute;left:0;right:0;top:300px;justify-content:center;color:var(--light-text);font-size:40px}
  .folder .url-band{position:absolute;left:0;right:0;bottom:0;height:44px;background:var(--band);color:var(--light-text);font-size:11px;letter-spacing:.2em;display:flex;align-items:center;justify-content:center}

  /* Business cards */
  .card{left:25px;width:180px;height:66px;overflow:hidden}
  .card-front{top:768px}
  .card-front .brand{font-size:9px;padding:9px 10px 0}
  .card-front .info{position:absolute;left:0;right:0;bottom:0;height:30px;background:var(--charcoal);color:var(--light-text);padding:5px 10px;font-size:5.5px;line-height:1.45}
  .card-front .info strong{font-size:6.5px;font-weight:700;letter-spacing:.05em}
  .card-back{top:842px}
  .card-back .brand{font-size:9px;padding:9px 10px 0}
  .card-back .tagline{position:absolute;left:0;right:0;bottom:12px;height:18px;background:var(--charcoal);color:var(--light-text);font-size:6.5px;letter-spacing:.06em;display:flex;align-items:center;padding-left:10px}

  /* Envelope front */
  .envelope-front{left:270px;top:768px;width:365px;height:140px}
  .envelope-front .brand{font-size:15px;padding:16px 20px 0}
  .envelope-front .return{font-size:6.5px;color:var(--muted);padding:6px 20px 0}
  .envelope-front .url-band{position:absolute;left:0;right:0;bottom:20px;height:18px;background:var(--charcoal);color:var(--light-text);font-size:7px;letter-spacing:.16em;display:flex;align-items:center;padding-left:20px}

  /* Envelope back */
  .envelope-back{left:665px;top:768px;width:510px;height:140px}
  .envelope-back svg{position:absolute;inset:0}
  .envelope-back .flap-url{position:absolute;left:0;right:0;top:16px;text-align:center;color:var(--light-text);font-size:9px;letter-spacing:.2em}
</style>
</head>
<body>

<section class="piece letterhead">
  <div class="brand"><span class="mark"></span>Harbor Summit Mentor</div>
  <div class="letter-body">
    <p>June 12, 2024</p>
    <p>Client Name<br>1200 Main Street, City State</p>
    <p class="gap">Thank you for taking the time to meet with our team this month. We enjoyed learning about your goals and the ways our coaching program can help your leaders grow with purpose, clarity and lasting confidence.</p>
    <p>Our sessions focus on listening, service and steady growth. Each plan is shaped around your people.</p>
    <p>We look forward to working with you and your team in the weeks ahead. Please reach out with any questions about the next steps or scheduling of the first workshop together.</p>
    <p>Best Regards,</p>
    <div class="signature" role="img" aria-label="Handwritten signature"></div>
    <p>Reed Calloway<br>Founder</p>
  </div>
  <footer class="letter-footer">
    <div class="address">4187 Willow Bend Lane Dallas TX 75231 &nbsp;|&nbsp; Phone 214 555 0187 &nbsp;|&nbsp; RCalloway@harborsummitmentor.example</div>
    <div class="url-band">www.HarborSummitMentor.example</div>
    <div class="base"></div>
  </footer>
</section>

<section class="piece folder">
  <div class="texture" role="img" aria-label="Dark woven texture pattern"></div>
  <div class="center-strip"></div>
  <div class="brand"><span class="mark"></span>Harbor Summit Mentor</div>
  <div class="url-band">www.HarborSummitMentor.example</div>
</section>

<section class="piece card card-front">
  <div class="brand"><span class="mark"></span>Harbor Summit Mentor</div>
  <div class="info">
    <strong>Reed Calloway</strong><br>
    Executive &amp; Professional Coach<br>
    RCalloway@harborsummitmentor.example
  </div>
</section>

<section class="piece card card-back">
  <div class="brand"><span class="mark"></span>Harbor Summit Mentor</div>
  <div class="tagline">Executive &amp; Professional Coaching</div>
</section>

<section class="piece envelope-front">
  <div class="brand"><span class="mark"></span>Harbor Summit Mentor</div>
  <div class="return">4187 Willow Bend Lane Dallas TX 75231</div>
  <div class="url-band">www.HarborSummitMentor.example</div>
</section>

<section class="piece envelope-back">
  <svg width="510" height="140" viewBox="0 0 510 140" aria-hidden="true">
    <polygon points="0,0 510,0 510,10 255,78 0,10" fill="#333"/>
    <line x1="0" y1="140" x2="255" y2="78" stroke="#dcdcdc" stroke-width="1"/>
    <line x1="510" y1="140" x2="255" y2="78" stroke="#dcdcdc" stroke-width="1"/>
  </svg>
  <div class="flap-url">www.HarborSummitMentor.example</div>
</section>

</body>
</html>
```